I would like a business card to match my truck wrap and logo. I would like the font to match my existing business card please.

Industry/Entity Type

Painter

Contact Information for Business Card

Rodrigo Venaza 801-437-2916 Venazacoatings.utah@brushmail.net
SERVICES - Custom Paint & Stain, Interior & Exterior, Epoxy Coatings / Garage Floors, Cabinet Refinishing, Log Staining and Refinishing.

Requirements
Nice to have
• I would like to have the white and grey line like the bottom of my vehicle wrap, Light Grey to match my truck also.

```html
<!DOCTYPE html>
<html lang="en">
<head>
<meta charset="utf-8">
<title>Venaza Coatings – Business Card</title>
<link rel="stylesheet" href="https://fonts.googleapis.com/css2?family=Saira+Condensed:wght@400;500&family=Source+Sans+3:wght@400;700&display=swap">
<style>
  :root {
    --navy: #045486;
    --ink: #0b5283;
    --mid-blue: #3f8fcb;
    --light-blue: #5aa4da;
    --deep-blue: #2a6fa6;
    --white: #ffffff;
    --card-line: #cfcfcf;
    --page: #ffffff;
  }
  * { margin: 0; padding: 0; box-sizing: border-box; }
  html, body { width: 1160px; height: 1200px; overflow: hidden; background: var(--page); }
  .canvas { position: relative; width: 1160px; height: 1200px; }

  .card { position: absolute; left: 195px; width: 737px; height: 460px; overflow: hidden; }
  .card--front { top: 95px; background: var(--navy); }
  .card--back { top: 639px; background: var(--white); border: 1px solid var(--card-line); }

  /* Front */
  .front-brand { position: absolute; left: 0; right: 0; top: 120px; display: flex; flex-direction: column; align-items: center; gap: 22px; }
  .front-brand__mark { width: 90px; height: 90px; background: var(--light-blue); border-radius: 10px; }
  .front-brand__name { font-family: "Source Sans 3", sans-serif; font-weight: 700; font-size: 44px; letter-spacing: 3px; color: var(--white); }

  .services-bar { position: absolute; left: 59px; top: 344px; width: 631px; height: 25px; }
  .services-bar__title { position: absolute; left: 72px; top: 343px; font-family: "Saira Condensed", sans-serif; font-weight: 500; font-size: 22px; letter-spacing: 6px; color: var(--navy); line-height: 27px; }
  .services-list { position: absolute; top: 380px; font-family: "Saira Condensed", sans-serif; font-size: 21px; color: var(--white); line-height: 33px; list-style: none; }
  .services-list--a { left: 70px; }
  .services-list--b { left: 295px; }
  .services-list--c { left: 462px; }

  /* Back */
  .back-brand { position: absolute; left: 92px; top: 122px; display: flex; align-items: center; gap: 24px; }
  .back-brand__mark { width: 70px; height: 70px; background: var(--mid-blue); border-radius: 8px; }
  .back-brand__name { font-family: "Source Sans 3", sans-serif; font-weight: 700; font-size: 52px; letter-spacing: 3px; color: var(--mid-blue); }

  .contact { position: absolute; right: 113px; top: 298px; text-align: right; font-family: "Source Sans 3", sans-serif; color: var(--ink); }
  .contact__name { font-weight: 700; font-size: 27px; line-height: 40px; }
  .contact__line { font-size: 24px; letter-spacing: 1.5px; line-height: 32px; position: relative; }
  .contact__icon { position: absolute; right: -32px; top: 6px; }

  .bottom-band { position: absolute; left: 0; top: 440px; width: 737px; height: 22px; }
</style>
</head>
<body>
<main class="canvas">

  <section class="card card--front" aria-label="Card front">
    <div class="front-brand">
      <div class="front-brand__mark"></div>
      <div class="front-brand__name">VENAZA COATINGS</div>
    </div>

    <svg class="services-bar" viewBox="0 0 631 25" aria-hidden="true">
      <polygon points="0,0 607,0 631,25 0,25" fill="var(--white)"/>
    </svg>
    <h2 class="services-bar__title">SERVICES</h2>

    <ul class="services-list services-list--a">
      <li>Custom Paint &amp; Stain</li>
      <li>Interior &amp; Exterior</li>
    </ul>
    <ul class="services-list services-list--b">
      <li>Epoxy Coatings</li>
      <li>Garage Floors</li>
    </ul>
    <ul class="services-list services-list--c">
      <li>Cabinet Refinishing</li>
      <li>Log Staining and Refinishing</li>
    </ul>
  </section>

  <section class="card card--back" aria-label="Card back">
    <div class="back-brand">
      <div class="back-brand__mark"></div>
      <div class="back-brand__name">VENAZA COATINGS</div>
    </div>

    <div class="contact">
      <p class="contact__name">Rodrigo Venaza</p>
      <p class="contact__line">801-437-2916
        <svg class="contact__icon" width="16" height="25" viewBox="0 0 16 25" aria-hidden="true">
          <rect x="1" y="1" width="14" height="23" rx="2.5" fill="none" stroke="var(--light-blue)" stroke-width="2"/>
          <rect x="3.5" y="4" width="9" height="14" fill="var(--light-blue)" opacity="0.35"/>
          <circle cx="8" cy="21" r="1.2" fill="var(--light-blue)"/>
        </svg>
      </p>
      <p class="contact__line">Venazacoatings.utah@brushmail.net
        <svg class="contact__icon" width="22" height="20" viewBox="0 0 22 20" aria-hidden="true">
          <polygon points="1,8 11,1 21,8 21,19 1,19" fill="none" stroke="var(--light-blue)" stroke-width="1.6"/>
          <polyline points="1,8 11,14 21,8" fill="none" stroke="var(--light-blue)" stroke-width="1.6"/>
          <text x="11" y="10" text-anchor="middle" font-size="7" font-family="Source Sans 3, sans-serif" fill="var(--light-blue)">@</text>
        </svg>
      </p>
    </div>

    <svg class="bottom-band" viewBox="0 0 737 22" preserveAspectRatio="none" aria-hidden="true">
      <defs>
        <linearGradient id="band-fade" x1="0" x2="1" y1="0" y2="0">
          <stop offset="0" stop-color="var(--deep-blue)"/>
          <stop offset="0.6" stop-color="var(--deep-blue)"/>
          <stop offset="1" stop-color="var(--light-blue)"/>
        </linearGradient>
      </defs>
      <polygon points="0,0 698,0 737,22 0,22" fill="url(#band-fade)"/>
    </svg>
  </section>

</main>
</body>
</html>
```